Gaming Related Website

GuildWeave.com is a forum for gamers to connect online.

We would like a design for our front page.

Please feel free to include a basic logo.

Please take a look at the following sites for inspiration:
http://uk.plaryx.com/
http://eu.fraygrid.net/en/
http://www.stormvantor.com/

Target Market(s)

On-line gamers on consoles and PCs

Industry/Entity Type

Online

Requirements
Must have
• Please follow the wireframes attached.

```html
<!DOCTYPE html>
<html lang="en">
<head>
<meta charset="utf-8">
<title>GuildWeave.com</title>
<link rel="stylesheet" href="https://fonts.googleapis.com/css2?family=Roboto:wght@400;500;700&display=swap">
<style>
:root{
  --ink:#1a1a1a;
  --white:#ffffff;
  --panel:#f2f2f2;
  --rule:#d2d2d2;
  --accent:#e8372c;
  --muted:#6a6a6a;
  --foot:#262424;
}
*{box-sizing:border-box;margin:0;padding:0}
html,body{width:1200px;height:1183px;overflow:hidden}
body{position:relative;font-family:"Roboto",Arial,sans-serif;color:var(--ink);background:#0d1412}
.abs{position:absolute}
.backdrop{left:0;top:0;width:1200px;height:1010px;
  background:
   radial-gradient(ellipse 420px 220px at 330px 170px,rgba(150,180,60,.55),transparent 70%),
   radial-gradient(ellipse 520px 260px at 620px 150px,rgba(120,150,40,.5),transparent 70%),
   radial-gradient(ellipse 500px 250px at 900px 760px,rgba(70,140,120,.45),transparent 70%),
   radial-gradient(ellipse 400px 240px at 180px 780px,rgba(40,110,80,.45),transparent 70%),
   linear-gradient(180deg,#0f2420 0%,#233d1f 25%,#10251f 60%,#0a1512 100%);}
.topbar{left:0;top:0;width:1200px;height:46px;background:linear-gradient(#1e1e1e,#050505)}
.brand{left:28px;top:10px;color:var(--white);font-weight:700;font-size:20px;letter-spacing:1px;display:flex;align-items:center;gap:6px}
.brand i{display:inline-block;width:10px;height:10px;background:var(--accent)}
.nav a{position:absolute;top:8px;color:var(--white);font-size:16px;text-decoration:none}
.nav small{display:block;font-size:12px;line-height:12px;color:#ddd}
.wordmark{left:28px;top:92px;color:var(--white);font-size:50px;font-weight:700;letter-spacing:2px}
.profile{left:825px;top:100px;width:375px;height:110px;background:linear-gradient(#2c2c2c,#0c0c0c)}
.avatar{left:8px;top:10px;width:92px;height:92px;border:1px solid #555;background:linear-gradient(#4a4a4a,#1a1a1a);color:var(--white);font-weight:700;font-size:26px;display:flex;align-items:center;justify-content:center}
.pname{left:130px;top:10px;color:var(--white);font-size:17px}
.prow{left:125px;top:34px;width:250px;height:14px;background:#080808;color:var(--white);font-size:12px;line-height:14px;padding-left:5px}
.prow b{color:var(--accent);font-weight:400}
.prow .sm{position:absolute;left:154px;font-size:8px;color:#ccc}
.plabel{left:130px;top:51px;color:#eee;font-size:12px}
.stat{top:70px;color:var(--white);font-size:15px;line-height:18px}
.stat span{display:block;font-size:12px}
.filter{left:220px;top:262px;width:450px;height:20px;background:linear-gradient(#3a3a3a,#161616);color:var(--white);font-size:11px;display:flex;align-items:center;gap:4px;padding-left:25px;white-space:nowrap}
.filter i{display:inline-block;width:10px;height:10px;background:#fff;margin-left:4px}
.tab{top:240px;width:153px;height:42px;background:linear-gradient(#353535,#0c0c0c);color:var(--white);font-size:15px;text-align:center;line-height:40px}
.tab svg{position:absolute;left:0;bottom:0}
.sidebar{left:0;top:282px;width:220px;height:398px;background:linear-gradient(90deg,#0c0c0c,#2e2e2e)}
.sidebar ul{list-style:none;padding-top:10px}
.sidebar li{height:45px;line-height:38px;color:var(--white);font-size:15px;text-align:center;margin:0 28px 0 25px;border-bottom:1px solid #3c3c3c;white-space:nowrap}
.sidebar li.wide{margin:0 10px}
.feed{left:220px;top:282px;width:757px;height:695px;background:var(--panel);border-bottom:6px solid #bdbdbd}
.item{position:absolute;left:40px;width:672px;text-align:center;font-size:15px;border-bottom:1px solid var(--rule)}
.btns{display:flex;justify-content:center;gap:12px;margin-top:14px}
.btn{font-size:14px;padding:1px 5px;background:linear-gradient(#e6e6e6,#c8c8c8);border:1px solid #bbb}
.btn.ok{border-color:#8fd08f}.btn.no{border-color:#e88}
.more{color:var(--muted);margin-top:18px}
.side{left:978px;width:222px;background:linear-gradient(#282828,#333)}
.stabs{height:19px;display:flex;background:#111}
.stabs div{flex:1;color:var(--white);font-size:12px;line-height:19px;text-align:center;background:linear-gradient(#3d3d3d,#1a1a1a);border-right:1px solid #555}
.side p{color:var(--white);font-size:12px;text-align:center}
.join{background:#444;color:var(--accent);padding:0 8px;margin-left:6px}
.footer{left:0;top:1010px;width:1200px;height:113px;background:var(--foot);color:var(--white);font-size:11.5px;text-align:center;padding-top:53px;border-top:1px solid #3a3a3a}
.legal{left:0;top:1123px;width:1200px;height:60px;background:linear-gradient(#2b2b2b,#151515);font-size:10.5px;color:#bbb}
.legal nav{position:absolute;left:220px;top:6px;display:flex;gap:11px}
.legal .copy{position:absolute;left:745px;top:6px}
.social{position:absolute;top:32px;width:18px;height:18px;background:#ddd;border-radius:3px}
</style>
</head>
<body>
<div class="abs backdrop" role="img" aria-label="Dark green smoky atmospheric game artwork background"></div>

<header class="abs topbar">
  <div class="abs brand"><i></i>GuildWeave</div>
  <nav class="nav">
    <a style="left:228px">Headlines</a>
    <a style="left:342px">Forum</a>
    <a style="left:432px">Communities</a>
    <a style="left:569px">Challenges</a>
    <a style="left:693px;top:9px;line-height:16px">Games<small>info&amp;download</small></a>
    <a style="left:816px">Competitions</a>
    <a style="left:952px">Achievements</a>
    <a style="left:1109px;top:6px">Teams</a>
  </nav>
</header>

<div class="abs wordmark">GuildWeave.com</div>

<section class="abs profile">
  <div class="abs avatar">GW</div>
  <div class="abs pname">Idle Epicure</div>
  <div class="abs prow"><b>E</b>dit &nbsp;&nbsp;&nbsp;<b>L</b>ogOut<span class="sm">Change Avatar</span></div>
  <div class="abs plabel">Gaming Stats</div>
  <div class="abs stat" style="left:130px">16<span>Games</span></div>
  <div class="abs stat" style="left:200px">3<span>Communities</span></div>
  <div class="abs stat" style="left:297px">2<span>Teams</span></div>
</section>

<div class="abs filter">Filter by: <i></i>Notifications <i></i>My Communities <i></i>My Teams <i></i>My competitions</div>
<div class="abs tab" style="left:670px">Newsfeed<svg width="26" height="10"><polygon points="0,0 26,10 0,10" fill="#e8372c"/></svg></div>
<div class="abs tab" style="left:824px">Chats<svg width="26" height="10"><polygon points="0,0 26,10 0,10" fill="#777"/></svg></div>

<aside class="abs sidebar">
  <ul>
    <li>All Games</li><li>Distant Rift</li><li>Edgelands 2</li><li>Shadow Oath III</li>
    <li class="wide">Line of Honor: Dark Ops 2</li><li>Realm Strife 2</li>
    <li class="wide">Valor Star Frontline</li><li style="border:0">Realm of Runecraft</li>
  </ul>
  <svg class="abs" style="left:85px;top:367px" width="50" height="12"><polyline points="1,1 25,10 49,1" fill="none" stroke="#e8372c"/></svg>
</aside>

<main class="abs feed">
  <div class="item" style="top:46px;height:76px">You've been challenged by Vantrix for a 1v1 game of Tremor Arena at 12:30 Today
    <div class="btns" style="gap:74px;margin-top:14px"><span class="btn" >Accept</span><span class="btn no">Decline</span></div></div>
  <div class="item" style="top:146px;height:76px">New Patch is out for Realm of Runecraft.<div class="more">Read More...</div></div>
  <div class="item" style="top:246px;height:42px">Pixa has posted in the “Team Quick Aim’s Private Board</div>
  <div class="item" style="top:313px;height:76px">You’ve been invited to join 40Strides gaming community link
    <div class="btns" style="gap:28px"><span class="btn ok">Accept</span><span class="btn no">Reject</span><span class="btn">Ignore</span></div></div>
  <div class="item" style="top:413px;height:42px">The Next PC SL3 match in SL3 4v4 Ladder has been canceled</div>
  <div class="item" style="top:480px;height:42px">Your application to join Comets of 40k team has been accepted</div>
  <div class="item" style="top:546px;height:42px">Veiled7 has accepted the invitation to become an admin of MS3 Mini League</div>
  <div class="item" style="top:613px;height:42px;border:0">Team Null Vector Crew has won against 40k comets in SL3 4v4 S&amp;D Ladder</div>
  <svg class="abs" style="left:352px;top:657px" width="50" height="12"><polyline points="1,1 25,10 49,1" fill="none" stroke="#e8372c"/></svg>
</main>

<section class="abs side" style="top:272px;height:199px">
  <div class="stabs"><div>Game servers</div><div>VOIP Channels</div></div>
  <p style="margin-top:11px">Stormline 3 ........32/18 <span class="join">Join</span></p>
  <p style="margin-top:131px;color:#ddd">Add a game server</p>
</section>
<section class="abs side" style="top:491px;height:199px">
  <div class="stabs"><div>My Communities</div><div>My Teams</div></div>
  <p style="margin-top:12px">PlayCircle.com......8 online</p>
  <p style="margin-top:131px;color:#ddd">Set up a community</p>
</section>

<footer class="abs footer">List of Members, filtered by game, community, team or any combination of the three. For just games the system will show how many players are online.</footer>
<div class="abs legal">
  <nav><span>Legal</span><span>Transparency &amp; Disclosure</span><span>Site Map</span><span>Contact Us</span></nav>
  <div class="copy">Copyright © 2012 VANTREK. All rights reserved.</div>
  <span class="social" style="left:934px"></span><span class="social" style="left:957px"></span>
</div>
</body>
</html>
```